依頼詳細
お好み焼き屋さんのTOPページのみのデザインをお願いしたいです。
コロナで減少したお客様を呼び戻すために試行錯誤しながら、このたびラーメンも提供することになりましたので、メインはお好み焼き屋さんですが、ラーメンも始めました!という画像付きで告知したいです。

集客を目的としたサイトです。
ターゲットは。お腹が空いた人になります!

レイアウト構成
・ヘッダー(ロゴのみ)
・TOP画像(画像はまだないのでフリーのもので大丈夫です)
・TOPページは画像だけでなくインパクトある感じを希望です(ザックリですみません。)
・お知らせ(3行程度)
・メニュー(テキストのみ)
・店舗情報(2店舗)テキスト
・フッター(下層ページないのでコピーライトぐらいでしょうか)
という構成です。
どこかにツマミドリと味ノートにリンクするボタンが欲しいです。
まだ素材がないため仮のフリー画像で構いません。

初心者の方でも大丈夫です!
今回は予算の都合上、低価格になってしまいましたがデザインのフィーリングが合う方は今後もご依頼する可能性があります!
サイトURL
ページ数
1ページ
希望イメージ
シンプル 複雑
単色 カラフル
暗い 明るい
日常 高級
遊び心 厳粛
未来的 伝統的
女性的 男性的
希望する色
無彩色系
納品ファイル
• 高解像度JPG (.jpg)
• イラストレーター形式 (.ai)
• フォトショップ形式 (.psd)
• PNG形式 (.png)
補足説明
納品はできれば、XDが希望です。
難しい場合はご相談ください。

お客様のイメージに一番近かったため選びました!

この度は、とても素晴らしいデザインのご提案をいただきまして誠にありがとうございました。
どれも捨てがたいデザインなのですが、一番イメージに近いものを選びました。
また、機会がございましたら、ご依頼をさせていただければと思います。
どうぞよろしくお願いいたします。

```html
<!DOCTYPE html>
<html lang="ja">
<head>
<meta charset="utf-8">
<title>炎山 | お好み焼き</title>
<link href="https://fonts.googleapis.com/css2?family=Noto+Serif+JP:wght@400;600;700&display=swap" rel="stylesheet">
<style>
:root{
  --ink:#0d0c0c;
  --night:#151413;
  --panel:#262423;
  --panel-line:#4a4644;
  --paper:#f3efe8;
  --muted:#a39d96;
  --red:#c0272d;
  --orange:#e0851f;
  --gold:#b89a4a;
}
*{box-sizing:border-box;margin:0;padding:0}
html,body{width:1200px;height:3276px;overflow:hidden;background:var(--ink)}
body{font-family:"Noto Serif JP",serif;color:var(--paper);position:relative}
.photo{position:absolute}

/* hero */
.hero{position:absolute;left:0;top:0;width:1200px;height:580px;background:var(--ink);overflow:hidden}
.hero-photo{left:380px;top:0;width:820px;height:580px;background:radial-gradient(ellipse at 60% 40%,#8a5a2c 0%,#4e2c17 45%,#1a120d 80%,var(--ink) 100%)}
.logo{position:absolute;left:40px;top:28px;display:flex;align-items:center;gap:12px}
.logo-mark{width:34px;height:34px;background:var(--red)}
.logo-name{font-size:48px;font-weight:700;color:var(--paper);letter-spacing:4px}
.hero-copy{position:absolute;left:40px;top:280px}
.hero-copy h1{font-size:34px;font-weight:600;line-height:1.5;letter-spacing:3px}
.hero-copy p{margin-top:16px;font-size:12px;line-height:1.9;color:var(--muted)}
.ramen-badge{position:absolute;left:830px;top:440px;display:flex;align-items:center;gap:14px}
.ramen-badge .bowl{width:110px;height:110px;border-radius:50%;background:radial-gradient(circle,#d9a35b 0%,#8b4a22 60%,#2b1b12 100%);border:3px solid var(--paper)}
.ramen-badge .txt{font-size:13px;line-height:1.5}
.ramen-badge .txt strong{display:block;font-size:28px;font-weight:700}
.ramen-badge .txt em{font-style:normal;font-size:20px;color:var(--paper)}

/* news */
.news{position:absolute;left:0;top:580px;width:1200px;height:420px;background:var(--night)}
.news h2{position:absolute;left:120px;top:70px;font-size:28px;font-weight:600;letter-spacing:4px}
.news h2 small{display:block;font-size:11px;color:var(--muted);letter-spacing:2px;margin-top:8px}
.news-icon{left:1000px;top:60px;width:80px;height:80px;border-radius:50%;background:#3a3532}
.news-list{position:absolute;left:120px;top:180px;width:960px;display:flex;gap:30px;list-style:none}
.news-list li{flex:1;border-top:1px solid var(--panel-line);border-left:1px solid var(--panel-line);padding:18px 20px 20px;height:150px;position:relative}
.news-list time{font-size:11px;color:var(--muted)}
.news-list p{margin-top:22px;font-size:13px;line-height:1.7}
.news-list a{position:absolute;right:20px;bottom:18px;font-size:11px;color:var(--muted);text-decoration:none}
.news-list a::before{content:"";display:inline-block;width:6px;height:6px;border-radius:50%;background:var(--red);margin-right:8px;vertical-align:middle}

/* menu */
.menu{position:absolute;left:0;top:1000px;width:1200px;height:1420px;background:var(--ink)}
.menu-photo{left:0;top:0;width:1200px;height:380px;background:linear-gradient(180deg,#2d2825 0%,#3b3431 55%,#1a1817 100%)}
.menu-panel{position:absolute;left:0;top:360px;width:1200px;height:1060px;background:var(--panel)}
.okonomi-photo{left:-220px;top:160px;width:540px;height:540px;border-radius:50%;background:radial-gradient(circle,#f1d27a 0%,#b87a3a 35%,#6b4a2e 70%,#3a3028 100%)}
.ramen-photo{left:900px;top:1120px;width:340px;height:340px;border-radius:50%;background:radial-gradient(circle,#e6b77a 0%,#a76a36 55%,#2a201b 100%)}
.teppan-sketch{left:60px;top:1080px;width:200px;height:180px;background:linear-gradient(135deg,#3a3735,#2a2827)}
.menu-title{position:absolute;right:140px;top:400px;display:flex;flex-direction:row-reverse;gap:10px;align-items:flex-start}
.menu-title small{writing-mode:vertical-rl;font-size:11px;color:var(--muted);letter-spacing:3px}
.menu-title h2{writing-mode:vertical-rl;font-size:44px;font-weight:600;letter-spacing:10px}
.menu-block{position:absolute;display:flex;flex-direction:row-reverse;align-items:flex-start;gap:30px}
.menu-block h3{writing-mode:vertical-rl;font-size:30px;font-weight:600;letter-spacing:6px}
.menu-block ul{list-style:none;display:flex;flex-direction:row-reverse;gap:20px;padding-right:30px;border-right:1px solid var(--panel-line);margin-top:20px}
.menu-block li{writing-mode:vertical-rl;height:340px;display:flex;justify-content:space-between;font-size:15px;letter-spacing:3px}
.blk-okonomi{right:240px;top:430px}
.blk-monja{right:560px;top:430px}
.blk-noodle{right:200px;top:990px}
.blk-drink{right:560px;top:990px}

/* shops */
.shops{position:absolute;left:0;top:2420px;width:1200px;height:760px;background:var(--ink)}
.shops-photo{left:0;top:0;width:1200px;height:760px;background:linear-gradient(180deg,#2a2220 0%,#1f1a18 50%,#0f0e0d 100%)}
.shops h2{position:absolute;left:584px;top:80px;writing-mode:vertical-rl;font-size:32px;font-weight:600;letter-spacing:8px}
.shop-list{position:absolute;left:220px;top:260px;display:flex;gap:60px;list-style:none}
.shop{width:380px;background:rgba(20,18,17,.85);border:1px solid var(--panel-line);padding:14px 14px 22px}
.shop-photo{position:relative;width:100%;height:190px;background:linear-gradient(135deg,#5a4a40,#2c2320)}
.shop-head{display:flex;justify-content:space-between;align-items:center;margin-top:18px}
.shop-head h3{font-size:16px;font-weight:600;letter-spacing:2px}
.shop-links{display:flex;gap:6px}
.shop-links a{display:block;width:26px;height:26px}
.shop-links .tsumamidori{background:var(--red)}
.shop-links .ajinote{background:var(--orange)}
.shop address{font-style:normal;font-size:11px;line-height:1.8;color:var(--muted);margin-top:10px}

/* footer */
.site-footer{position:absolute;left:0;top:3180px;width:1200px;height:96px;background:var(--ink);border-top:3px solid var(--gold);display:flex;align-items:center;justify-content:center}
.site-footer small{font-size:11px;color:var(--muted);letter-spacing:1px}
</style>
</head>
<body>

<header class="hero">
  <div class="photo hero-photo" role="img" aria-label="鉄板で焼き上がったお好み焼きの写真"></div>
  <div class="logo"><span class="logo-mark"></span><span class="logo-name">炎山</span></div>
  <div class="hero-copy">
    <h1>「味・食感・香り」<br>すべてに自信があります。</h1>
    <p>当店は、「味・食感・香り」にこだわりぬいた、本場の味を提供します。<br>焼き上がりの音と香りで、空腹のお客様を笑顔にいたします。</p>
  </div>
  <div class="ramen-badge">
    <div class="bowl" role="img" aria-label="塩ラーメンの写真"></div>
    <div class="txt">ラーメン始めました<strong>塩ラーメン</strong><em>一杯 850円</em></div>
  </div>
</header>

<section class="news">
  <h2>お知らせ<small>NEWS</small></h2>
  <div class="photo news-icon" role="img" aria-label="小さなお好み焼きのイラスト"></div>
  <ul class="news-list">
    <li><time>2021.02.15</time><p>本日サイトをリニューアルしました</p><a href="#">詳しく見る</a></li>
    <li><time>2021.02.10</time><p>年末年始の営業時間について</p><a href="#">詳しく見る</a></li>
    <li><time>2021.02.01</time><p>感染症対策のため営業時間・定休日の変更</p><a href="#">詳しく見る</a></li>
  </ul>
</section>

<section class="menu">
  <div class="photo menu-photo" role="img" aria-label="鉄板と店内の写真"></div>
  <div class="menu-panel"></div>
  <div class="photo okonomi-photo" role="img" aria-label="目玉焼きをのせたお好み焼きの写真"></div>
  <div class="photo ramen-photo" role="img" aria-label="ラーメンの写真"></div>
  <div class="photo teppan-sketch" role="img" aria-label="鉄板焼きの手描きイラスト"></div>

  <div class="menu-title"><small>MENU</small><h2>お品書き</h2></div>

  <div class="menu-block blk-okonomi"><h3>お好み焼き</h3>
    <ul><li>豚玉<span>¥1200</span></li><li>牛筋ねぎ焼き<span>¥1300</span></li><li>広島焼<span>¥1100</span></li><li>ミックスお好み焼き<span>¥1500</span></li></ul>
  </div>
  <div class="menu-block blk-monja"><h3>もんじゃ焼き</h3>
    <ul><li>牛筋もんじゃ<span>¥850</span></li><li>明太もち<span>¥1100</span></li><li>ミックスもんじゃ<span>¥1300</span></li></ul>
  </div>
  <div class="menu-block blk-noodle"><h3>麺類</h3>
    <ul><li>焼きそば<span>¥1200</span></li><li>塩ラーメン<span>¥850</span></li><li>焼うどん<span>¥1100</span></li></ul>
  </div>
  <div class="menu-block blk-drink"><h3>飲み物</h3>
    <ul><li>生ビール<span>¥500</span></li><li>烏龍茶<span>¥350</span></li><li>レモンサワー<span>¥450</span></li></ul>
  </div>
</section>

<section class="shops">
  <div class="photo shops-photo" role="img" aria-label="暖簾のかかった店先の写真"></div>
  <h2>店舗情報</h2>
  <ul class="shop-list">
    <li class="shop">
      <div class="shop-photo" role="img" aria-label="本店の店先の写真"></div>
      <div class="shop-head"><h3>炎山 川辺本店</h3>
        <div class="shop-links"><a class="tsumamidori" href="#" aria-label="ツマミドリ"></a><a class="ajinote" href="#" aria-label="味ノート"></a></div></div>
      <address>〒100-0123<br>架空県川辺市中町一丁目2番3号</address>
    </li>
    <li class="shop">
      <div class="shop-photo" role="img" aria-label="港店の店内の写真"></div>
      <div class="shop-head"><h3>炎山 港店</h3>
        <div class="shop-links"><a class="tsumamidori" href="#" aria-label="ツマミドリ"></a><a class="ajinote" href="#" aria-label="味ノート"></a></div></div>
      <address>〒100-0456<br>架空県港市浜通り四丁目5番6号</address>
    </li>
  </ul>
</section>

<footer class="site-footer"><small>Copyright © Enzan All Rights Reserved.</small></footer>

</body>
</html>
```